Business Coach needs an elegant business card design

I need a business card design based around my logo for color and to look like a millionaire dollar coach. Incorporate the color of my logo with something creative and attractive that stands out. I am focused on high end companies and the card must look and feel that way.

Target Market(s)

High End Companies and Business Owners - Training People to become millionaires

Industry/Entity Type

Business

Requirements
Must have
• Front -
Logo (attached file) - Website (kolverbask.com) - Name (Darvel Kemp) Phone (412.807.5531) - Email (darvel@kolverbask.com) (My Title - Success Coach)
Back -
Slogan - Vision (see it) . Action (do it) . Transformation (be it)
Website - Learn More @ kolverbask.com

Creative High End Look!
Nice to have
Should not have
• Cheap standard look
nothing traditional

```html
<!DOCTYPE html>
<html lang="en">
<head>
<meta charset="utf-8">
<title>Darvel Kemp Coaching — Business Card</title>
<link rel="stylesheet" href="https://fonts.googleapis.com/css2?family=Cinzel:wght@400;600;700&display=swap">
<style>
  :root {
    --navy: #141f4a;
    --navy-deep: #0f1840;
    --white: #ffffff;
    --ring-grey: #d6d7dd;
    --text-grey: #6b6e78;
    --stage: #3b3b3d;
  }
  * { margin: 0; padding: 0; box-sizing: border-box; }
  html, body {
    width: 1200px; height: 750px; overflow: hidden;
    background: var(--stage);
    font-family: "Cinzel", "Times New Roman", serif;
  }
  .canvas { position: relative; width: 1200px; height: 750px; }
  .card {
    position: absolute; top: 218px; width: 493px; height: 282px; overflow: hidden;
  }

  /* Front */
  .card-front { left: 91px; background: var(--white); }
  .front-watermark { position: absolute; left: 0; top: 0; }
  .name-band {
    position: absolute; left: 0; top: 31px; width: 262px; height: 53px;
    background: var(--navy);
  }
  .holder { position: absolute; left: 38px; top: 40px; color: var(--white); }
  .holder-name { font-size: 17px; font-weight: 600; letter-spacing: 0.5px; line-height: 1; }
  .holder-title { font-size: 11px; letter-spacing: 1px; margin-top: 4px; }
  .front-mark {
    position: absolute; left: 236px; top: 32px; width: 52px; height: 52px;
    border-radius: 50%; background: var(--navy); border: 3px solid var(--white);
    box-shadow: 0 0 0 2px var(--navy);
  }
  .front-brand {
    position: absolute; left: 297px; top: 40px; color: var(--navy);
    font-weight: 600; text-align: center; line-height: 1;
  }
  .front-brand .brand-main { display: block; font-size: 20px; letter-spacing: 0.5px; }
  .front-brand .brand-sub { display: block; font-size: 12px; letter-spacing: 3px; margin-top: 4px; }
  .contact { position: absolute; left: 33px; top: 185px; list-style: none; }
  .contact li { font-size: 11px; line-height: 20px; color: var(--text-grey); }
  .contact .label { display: inline-block; width: 26px; color: var(--navy); font-weight: 700; }

  /* Back */
  .card-back { left: 620px; background: var(--navy); }
  .web-band {
    position: absolute; left: 25px; right: 25px; top: 37px; height: 26px;
    background: linear-gradient(90deg, rgba(255,255,255,0) 0%, rgba(255,255,255,0.12) 50%, rgba(255,255,255,0) 100%);
    border-top: 1px solid rgba(255,255,255,0.35);
    border-bottom: 1px solid rgba(255,255,255,0.15);
    display: flex; align-items: center; justify-content: center;
  }
  .web-cta { color: var(--white); font-size: 12px; font-weight: 700; font-style: italic; letter-spacing: 0.5px; }
  .back-logo {
    position: absolute; left: 0; right: 0; top: 107px;
    display: flex; align-items: center; justify-content: center; gap: 12px;
  }
  .back-mark {
    width: 70px; height: 70px; border-radius: 50%;
    border: 4px solid var(--white); background: var(--navy-deep);
  }
  .back-brand { color: var(--white); font-weight: 600; text-align: center; line-height: 1; }
  .back-brand .brand-main { display: block; font-size: 26px; letter-spacing: 0.5px; }
  .back-brand .brand-sub { display: block; font-size: 15px; letter-spacing: 3px; margin-top: 5px; }
  .slogan {
    position: absolute; left: 0; right: 0; top: 211px; list-style: none;
    text-align: center; color: var(--white);
  }
  .slogan li { font-size: 12px; line-height: 14.5px; letter-spacing: 0.5px; }
  .slogan strong { font-weight: 700; }
  .slogan .final { font-style: italic; }
</style>
</head>
<body>
<main class="canvas">

  <section class="card card-front" aria-label="Card front">
    <svg class="front-watermark" width="493" height="282" viewBox="0 0 493 282" aria-hidden="true">
      <circle cx="385" cy="258" r="142" fill="none" stroke="var(--ring-grey)" stroke-width="10"/>
      <circle cx="385" cy="258" r="120" fill="var(--ring-grey)"/>
    </svg>
    <div class="name-band"></div>
    <div class="holder">
      <p class="holder-name">Darvel Kemp</p>
      <p class="holder-title">Success Coach</p>
    </div>
    <div class="front-mark" aria-hidden="true"></div>
    <p class="front-brand"><span class="brand-main">Darvel Kemp</span><span class="brand-sub">Coaching</span></p>
    <ul class="contact">
      <li><span class="label">P :</span>412.807.5531</li>
      <li><span class="label">E :</span>darvel@kolverbask.com</li>
      <li><span class="label">W :</span>kolverbask.com</li>
    </ul>
  </section>

  <section class="card card-back" aria-label="Card back">
    <div class="web-band"><p class="web-cta">Learn More @ kolverbask.com</p></div>
    <div class="back-logo">
      <div class="back-mark" aria-hidden="true"></div>
      <p class="back-brand"><span class="brand-main">Darvel Kemp</span><span class="brand-sub">Coaching</span></p>
    </div>
    <ul class="slogan">
      <li><strong>VISION</strong> - See What You Want</li>
      <li><strong>ACTION</strong> - Do What It Takes</li>
      <li class="final"><strong>TRANSFORMATION</strong> - Live Your Vision!</li>
    </ul>
  </section>

</main>
</body>
</html>
```